Business card and Stationery for data intelligence company

We need a new design for our business cards and stationery (Business Letter templates and a Quote example on Word, but it MUST work on Google Doc as well).

We are a software company based in Ireland and UK. Our product is "Kovar", data intelligence platform with beautiful visualizations, graph capabilities (things are interconnected), powerful, flexible, it can manage Big Data and Streaming information. It's modern and relatively open source.
Our company will provide data intelligence for law enforcements, pharmaceuticals, and similar high end customers.

We'll launch a new website soon. At the moment it's http://www.kovar-analytics.example if you want to take a look. This is our youtube channel in case you need it to understand what Kovar is: https://www.youtube.com/c/kovaranalyticschannel

We changed the logo so please use the logo I attach here.

We'd like the output to be cool and modern but elegant and "business" at the same time. It should inspire simple sophistication, "unity" "intent" "purpose" yet subtly very advanced and innovative.

The name "Kovar" does NOT refer to sirens (mithological creatures) as well as the warning devices. It means Kinetic Object Vector Analysis Reactor. Please use our logo's colors and if you want to something like the "graph" image.

```html
<!DOCTYPE html>
<html lang="en">
<head>
<meta charset="utf-8">
<title>Kovar – Business Card</title>
<link href="https://fonts.googleapis.com/css2?family=Lato:wght@400;700&display=swap" rel="stylesheet">
<style>
  :root {
    --stage: #0a74ae;
    --card: #2e2e2e;
    --card-mark: #3f3f3f;
    --accent: #f5b335;
    --ink-light: #ffffff;
    --ink-soft: #e6e6e6;
  }
  * { margin: 0; padding: 0; box-sizing: border-box; }
  html, body { width: 1200px; height: 1000px; overflow: hidden; }
  body {
    position: relative;
    background: var(--stage);
    font-family: "Lato", Arial, sans-serif;
  }
  .card {
    position: absolute;
    left: 318px;
    width: 567px;
    background: var(--card);
    overflow: hidden;
  }
  .card--front { top: 92px; height: 407px; }
  .card--back { top: 515px; height: 392px; }

  .card__mark {
    position: absolute;
    border-radius: 50%;
    border: 30px solid var(--card-mark);
  }
  .card--front .card__mark { left: 138px; top: 48px; width: 300px; height: 300px; }
  .card--back .card__mark { left: 135px; top: 50px; width: 300px; height: 300px; }

  .brand {
    position: absolute;
    display: flex;
    align-items: center;
  }
  .brand__dot { border-radius: 50%; flex: none; }
  .brand__name { font-weight: 400; line-height: 1; }

  .card--front .brand { left: 126px; top: 158px; gap: 30px; }
  .card--front .brand__dot { width: 80px; height: 80px; background: var(--ink-light); }
  .card--front .brand__name { color: var(--ink-light); font-size: 54px; letter-spacing: 6px; }

  .card--back .brand { left: 30px; top: 32px; gap: 16px; }
  .card--back .brand__dot { width: 74px; height: 74px; background: var(--accent); }
  .card--back .brand__name { color: var(--accent); font-size: 42px; letter-spacing: 5px; }

  .social {
    position: absolute;
    right: 30px;
    top: 48px;
    display: flex;
    gap: 3px;
  }
  .social__item { width: 16px; height: 16px; background: var(--accent); }

  .person {
    position: absolute;
    right: 40px;
    top: 230px;
    text-align: right;
    padding-right: 10px;
    border-right: 2px solid var(--accent);
  }
  .person__name { color: var(--accent); font-weight: 700; font-size: 23px; line-height: 1.05; }
  .person__role { color: var(--ink-light); font-size: 17px; line-height: 1.2; }

  .address {
    position: absolute;
    left: 30px;
    top: 304px;
    color: var(--ink-soft);
    font-size: 16px;
    line-height: 20.5px;
    font-style: normal;
  }

  .contacts {
    position: absolute;
    right: 30px;
    top: 304px;
    list-style: none;
  }
  .contacts__item {
    display: flex;
    justify-content: flex-end;
    align-items: center;
    gap: 6px;
    color: var(--ink-soft);
    font-size: 16px;
    line-height: 20.5px;
  }
  .contacts__icon {
    width: 17px; height: 17px;
    background: var(--accent);
    display: flex; align-items: center; justify-content: center;
  }
</style>
</head>
<body>
  <section class="card card--front">
    <div class="card__mark" aria-hidden="true"></div>
    <div class="brand">
      <span class="brand__dot"></span>
      <span class="brand__name">KOVAR</span>
    </div>
  </section>

  <section class="card card--back">
    <div class="card__mark" aria-hidden="true"></div>
    <div class="brand">
      <span class="brand__dot"></span>
      <span class="brand__name">KOVAR</span>
    </div>

    <div class="social" aria-label="Social profiles">
      <span class="social__item"></span>
      <span class="social__item"></span>
      <span class="social__item"></span>
    </div>

    <div class="person">
      <p class="person__name">Daniel Reyes</p>
      <p class="person__role">CEO</p>
    </div>

    <address class="address">
      Unit 7<br>
      Harbourview Business Park<br>
      Renmore, Galway - Ireland
    </address>

    <ul class="contacts">
      <li class="contacts__item">+353 87 5550142
        <span class="contacts__icon">
          <svg width="11" height="11" viewBox="0 0 24 24"><path fill="#2e2e2e" d="M6.6 10.8a15 15 0 0 0 6.6 6.6l2.2-2.2c.3-.3.7-.4 1-.2 1.1.4 2.3.6 3.6.6.6 0 1 .4 1 1V20c0 .6-.4 1-1 1A17 17 0 0 1 3 4c0-.6.4-1 1-1h3.5c.6 0 1 .4 1 1 0 1.3.2 2.5.6 3.6.1.3 0 .7-.2 1z"/></svg>
        </span>
      </li>
      <li class="contacts__item">www.kovar-analytics.example
        <span class="contacts__icon">
          <svg width="11" height="11" viewBox="0 0 24 24"><rect x="2" y="3" width="20" height="14" rx="1" fill="none" stroke="#2e2e2e" stroke-width="2.5"/><path d="M8 21h8M12 17v4" stroke="#2e2e2e" stroke-width="2.5"/></svg>
        </span>
      </li>
      <li class="contacts__item">info@kovar-analytics.example
        <span class="contacts__icon">
          <svg width="11" height="11" viewBox="0 0 24 24"><rect x="2" y="5" width="20" height="14" fill="#2e2e2e"/><path d="M2 5l10 8 10-8" fill="none" stroke="#f5b335" stroke-width="2"/></svg>
        </span>
      </li>
    </ul>
  </section>
</body>
</html>
```